new website screendesign for real estate company

We need new website design
The design must fit into the Corporate Identity design of the company.

old page
http://www.wohnkarta.at/

we made some layout.png where you can see the components
http://93.12.204.17:8080/Layout.png
+ its attached

dont design exactly like this we just copied different things together. you can design anything new

the layout.png should just show you the direction. and you can see the basic structure of the page

upper left logo upper right login
navigation
banner slider
search filter

carousel with top objects (real estate)

the lower 4 points are predefined search results. for example when "für Anspruchsvolle" is clicked all luxury objects are displayed
when "WG geeignet" is clicked it shows objects for low budget and students.

also find fitting images for all the once used in layout.png are quite bad

here are some of our previous real estate projects

http://93.12.88.6:8082/brelt/
http://www.quirba.at/
http://www.lerchen-immobilien.at/

```html
<!DOCTYPE html>
<html lang="en">
<head>
<meta charset="utf-8">
<title>Dr. Keltmayr Immobilien GmbH</title>
<link href="https://fonts.googleapis.com/css2?family=Open+Sans:wght@400;600;700&family=Oswald:wght@500&display=swap" rel="stylesheet">
<style>
:root{
  --tan:#f3c9a0;
  --red:#e2401c;
  --red-dark:#c9350f;
  --navy:#0f1a3a;
  --text:#444;
  --muted:#888;
  --sand:#bdb5a6;
  --line:#e2e2e2;
  --blue-link:#2a8cc8;
}
*{box-sizing:border-box;margin:0;padding:0}
html,body{width:1200px;height:2383px;overflow:hidden}
body{font-family:"Open Sans",sans-serif;color:var(--text);background:#fff;position:relative}
.abs{position:absolute}

/* header */
.topbar{left:0;top:0;width:1200px;height:67px;background:var(--tan)}
.topbar .marker{left:280px;top:0;width:28px;height:4px;background:var(--red)}
.nav{left:275px;top:0;height:67px;display:flex;align-items:center;gap:26px;font-size:13px;color:#333}
.search-icon{left:952px;top:26px}
.brand{left:105px;top:0;width:158px;height:122px;border-radius:0 0 79px 79px;background:var(--tan);display:flex;align-items:center;justify-content:center;z-index:3}
.brand-oval{width:132px;height:66px;border-radius:50%;background:#fff;border:3px solid var(--red);display:flex;align-items:center;justify-content:center;gap:6px}
.brand-oval .sq{width:10px;height:10px;background:var(--red)}
.brand-oval span{font-size:14px;font-weight:600;color:#555}

/* hero */
.hero{left:0;top:67px;width:1200px;height:453px;background:linear-gradient(180deg,#0c1432 0%,#1d2b4c 35%,#8a96a0 62%,#3f5a3a 82%,#24331f 100%)}
.hero-title{left:0;top:98px;width:1290px;text-align:center;font-family:"Oswald",sans-serif;font-weight:500;font-size:44px;line-height:64px;letter-spacing:2px;color:#fff}
.anniv{left:1014px;top:76px;width:162px;height:156px;border-radius:50%;background:radial-gradient(circle,#e9b54a 0%,#b97d1c 70%,#8a5a10 100%)}
.big-search{left:248px;top:247px;width:741px;height:57px;background:#fff;border-radius:4px;display:flex;align-items:center}
.big-search .ph{margin-left:50px;font-size:19px;color:#666}
.big-search .go{position:absolute;right:3px;top:3px;width:107px;height:51px;background:var(--red);border-radius:3px;display:flex;align-items:center;justify-content:center}
.big-search .lens{position:absolute;left:16px;top:18px}
.filter{top:357px;width:277px}
.filter label{display:block;font-size:12px;font-weight:700;color:#fff;margin-bottom:5px}
.filter .field{height:32px;background:#fff;border-radius:2px;font-size:11px;color:#bbb;padding:9px 8px}
.filter-go{left:1028px;top:379px;width:52px;height:32px;background:var(--red);border-radius:2px;display:flex;align-items:center;justify-content:center}
.dots{left:1181px;top:353px}
.dots i{display:block;width:6px;height:6px;border-radius:50%;border:1px solid #fff;margin-bottom:11px}
.dots i.on{background:#fff}
.hero-shadow{left:0;top:520px;width:1200px;height:30px;background:radial-gradient(ellipse at 50% 0%,rgba(0,0,0,.25),rgba(0,0,0,0) 70%)}

/* address */
.address-title{left:0;top:566px;width:1184px;text-align:center;color:var(--red);font-weight:700;font-size:21px}
.list{top:628px;font-size:14px;line-height:29px;color:#555}
.list li{list-style:none}

/* featured */
.featured{left:0;top:756px;width:1200px;height:451px;background:linear-gradient(135deg,#cbc4b6 0%,#b7af9f 50%,#c6bfb2 100%)}
.featured h2{position:absolute;top:50px;width:1240px;text-align:center;font-size:26px;line-height:28px;font-weight:600;color:var(--red)}
.featured .sub{position:absolute;top:79px;width:1210px;text-align:center;font-size:16px;line-height:20px;font-weight:700;letter-spacing:1.5px;color:#333}
.card{top:167px;width:207px;height:130px;border:4px solid #fff;box-shadow:0 0 18px rgba(255,255,255,.8)}
.portfolio{left:551px;top:361px;width:113px;height:32px;background:var(--red);border-radius:3px;color:#fff;font-size:13px;font-weight:700;display:flex;align-items:center;justify-content:center}

/* group band */
.band{left:0;top:1207px;width:1200px;height:74px;background:var(--red)}
.band .name{position:absolute;left:197px;top:23px;font-size:18px;font-weight:700;letter-spacing:1.5px;color:#fff}
.tab{position:absolute;top:24px;height:30px;font-size:10px;font-weight:700;color:#fff;display:flex;align-items:center;justify-content:center}
.tab.on{border:2px solid #fff;border-radius:16px;width:105px}

/* news */
.news-box{left:171px;top:1307px;width:877px;height:213px;border:1px solid var(--line);background:#fff}
.news-img{top:1355px;width:168px;height:104px}
.news h4{font-size:12px;font-weight:600;color:var(--blue-link);margin-bottom:10px}
.news p{font-size:11px;line-height:16px;color:#333}
.arrow-sq{width:34px;height:36px;background:var(--red);display:flex;align-items:center;justify-content:center}
.pager{left:590px;top:1484px;display:flex;gap:4px}
.pager i{width:15px;height:15px;border-radius:50%;background:var(--red);display:flex;align-items:center;justify-content:center}

/* partners */
.partners{left:165px;top:1575px;width:878px;height:89px;border:1px solid var(--line)}
.partner{top:1593px;height:52px;border-radius:6px;background:#dde3e8}

/* contact */
.touch{left:0;top:1711px;width:1200px;height:230px;background:var(--red);color:#fff;text-align:center}
.touch h2{position:absolute;top:60px;width:1192px;font-size:29px;font-weight:600}
.touch .rule{position:absolute;left:285px;top:114px;width:622px;height:1px;background:rgba(255,255,255,.55)}
.touch .knot{position:absolute;left:587px;top:106px;width:16px;height:16px;border-radius:50%;border:1px solid rgba(255,255,255,.8);background:var(--red)}
.touch p{position:absolute;left:380px;top:138px;width:432px;font-size:10.5px;line-height:19px}
.map{left:0;top:1941px;width:1200px;height:322px;background:linear-gradient(160deg,#eeeeee 0%,#e3e3e3 50%,#ebebeb 100%)}
.pin{left:564px;top:1909px;width:64px;height:64px;border-radius:50%;background:var(--red);border:4px solid #fff;display:flex;align-items:center;justify-content:center}
.info{left:527px;top:2017px;width:357px;height:131px;background:#fff;box-shadow:0 2px 8px rgba(0,0,0,.15)}
.info .mark{position:absolute;left:0;top:0;width:118px;height:131px;background:var(--navy);display:flex;align-items:center;justify-content:center;gap:5px}
.info .mark i{width:8px;height:8px;background:#4a7bd1}
.info .mark span{font-size:13px;font-weight:600;color:#4a7bd1}
.info ul{position:absolute;left:130px;top:12px;list-style:none;font-size:10.5px;line-height:16px;color:#444}
.info li{display:flex;gap:8px;margin-bottom:12px}
.info li.mail{color:var(--red)}

/* footer */
.footer{left:0;top:2263px;width:1200px;height:57px;background:var(--tan)}
.footer nav{position:absolute;left:170px;top:20px;display:flex;gap:16px;font-size:12px;color:#333}
.lang{position:absolute;left:963px;top:15px;width:74px;height:26px;background:#fff;border-radius:3px;font-size:10px;color:#555;display:flex;align-items:center;justify-content:center;gap:4px}
.base{left:0;top:2320px;width:1200px;height:63px;background:var(--red)}
</style>
</head>
<body>

<!-- header -->
<div class="abs topbar"></div>
<div class="abs topbar marker"></div>
<nav class="abs nav"><span>About</span><span>Company info</span><span>Companies</span><span>Projects</span><span>Deals</span><span>Media center</span><span>Career</span><span>Contact</span></nav>
<svg class="abs search-icon" width="18" height="18" viewBox="0 0 18 18"><circle cx="7.5" cy="7.5" r="6" fill="none" stroke="#555" stroke-width="1.5"/><line x1="12" y1="12" x2="17" y2="17" stroke="#555" stroke-width="1.5"/></svg>

<!-- hero -->
<div class="abs hero" role="img" aria-label="Night view of residential high-rise towers with palm trees in front"></div>
<div class="abs brand"><div class="brand-oval"><i class="sq"></i><span>WOHNKARTA</span></div></div>
<h1 class="abs hero-title">DR.KELTMAYR IMMOBILIEN GMBH</h1>
<div class="abs anniv" role="img" aria-label="Gold fifteen years anniversary seal"></div>
<div class="abs big-search">
  <svg class="lens" width="20" height="20" viewBox="0 0 20 20"><circle cx="8" cy="8" r="6.5" fill="none" stroke="#999" stroke-width="1.6"/><line x1="13" y1="13" x2="19" y2="19" stroke="#999" stroke-width="1.6"/></svg>
  <span class="ph">Enter your city or zipcode here...</span>
  <div class="go"><svg width="24" height="24" viewBox="0 0 24 24"><circle cx="10" cy="10" r="7" fill="none" stroke="#fff" stroke-width="3.2"/><line x1="15" y1="15" x2="21" y2="21" stroke="#fff" stroke-width="3.5" stroke-linecap="round"/></svg></div>
</div>
<div class="abs filter" style="left:203px"><label>Location Name</label><div class="field">Secunderabad</div></div>
<div class="abs filter" style="left:503px"><label>Restaurant Name</label><div class="field">Lakeside Grand</div></div>
<div class="abs filter" style="left:803px;width:203px"><label>Cuisine Name</label><div class="field">Chicken Biriyani</div></div>
<div class="abs filter-go"><svg width="16" height="16" viewBox="0 0 16 16"><circle cx="6.5" cy="6.5" r="4.5" fill="none" stroke="#fff" stroke-width="2.4"/><line x1="10" y1="10" x2="14.5" y2="14.5" stroke="#fff" stroke-width="2.6" stroke-linecap="round"/></svg></div>
<div class="abs dots"><i class="on"></i><i></i><i></i></div>
<div class="abs hero-shadow"></div>

<!-- address -->
<h2 class="abs address-title">1450 MARLOWE AVENUE,PINE TERRACE</h2>
<ul class="abs list" style="left:92px">
  <li>o Bayline contracting: The most important part, the main real e-state company.</li>
  <li>o Sahrani House: Furniture retails store and gallery.</li>
  <li>o Sahrani Training Center.</li>
</ul>
<ul class="abs list" style="left:660px">
  <li>o Sahrani Gym (Currently opening this month).</li>
  <li>o Oasis Palace.</li>
  <li>o VENTARA.</li>
</ul>

<!-- featured projects -->
<section class="abs featured">
  <h2>Featured Projects.</h2>
  <div class="sub">Sahrani Group CompanyReal Estate Service · Real Estate Investment</div>
  <div class="abs card" style="left:133px;background:linear-gradient(180deg,#7fb0e0 0%,#d9d6cc 45%,#6f9a3e 100%)" role="img" aria-label="Apartment towers behind a lawn"></div>
  <div class="abs card" style="left:393px;background:linear-gradient(180deg,#6d9ad6 0%,#e3d9c0 55%,#6b6b6b 100%)" role="img" aria-label="Row of townhouses along a street"></div>
  <div class="abs card" style="left:644px;background:linear-gradient(180deg,#9cc0ec 0%,#8aa0b8 50%,#9b7a62 100%)" role="img" aria-label="Modern glass office building"></div>
  <div class="abs card" style="left:897px;background:linear-gradient(180deg,#8fc065 0%,#e6e6e6 50%,#4f8a2e 100%)" role="img" aria-label="Detached family house with garden"></div>
  <div class="abs portfolio">View Portfolio</div>
</section>

<!-- group band -->
<div class="abs band">
  <div class="name">Sahrani Group Company</div>
  <div class="tab on" style="left:505px">FEATURED NEWS</div>
  <div class="tab" style="left:659px">FEATURED EVENTS</div>
  <div class="tab" style="left:810px">LANGUAGE SWITCHING</div>
</div>

<!-- news -->
<div class="abs news-box"></div>
<div class="abs news-img" style="left:209px;background:linear-gradient(180deg,#f2f2f2 0%,#c7c0b8 50%,#6d8bb0 100%)" role="img" aria-label="Group of young friends posing together"></div>
<div class="abs news" style="left:395px;top:1360px;width:200px">
  <h4>Another post title goes here</h4>
  <p>This is Photoshop's version&nbsp; of Lorem Ipsum. Proin gravida nibh vel velit auctor aliquet. Aenean sollicitudin, lorem quis bibendum auctor...</p>
</div>
<div class="abs news-img" style="left:629px;background:linear-gradient(180deg,#f2f2f2 0%,#c7c0b8 50%,#6d8bb0 100%)" role="img" aria-label="Group of young friends posing together"></div>
<div class="abs news" style="left:815px;top:1362px;width:210px">
  <h4>Post title goeas here</h4>
  <p>In the recent months, we have begun to attract more and more members to our site. Finally we a re beginning to see some activity in our...</p>
</div>
<div class="abs arrow-sq" style="left:157px;top:1393px"><svg width="10" height="14" viewBox="0 0 10 14"><polyline points="7,2 2,7 7,12" fill="none" stroke="#fff" stroke-width="1.6"/></svg></div>
<div class="abs arrow-sq" style="left:1025px;top:1393px"><svg width="10" height="14" viewBox="0 0 10 14"><polyline points="3,2 8,7 3,12" fill="none" stroke="#fff" stroke-width="1.6"/></svg></div>
<div class="abs pager">
  <i><svg width="9" height="9" viewBox="0 0 9 9"><polyline points="6,1 2.5,4.5 6,8" fill="none" stroke="#fff" stroke-width="1.8"/></svg></i>
  <i><svg width="9" height="9" viewBox="0 0 9 9"><polyline points="3,1 6.5,4.5 3,8" fill="none" stroke="#fff" stroke-width="1.8"/></svg></i>
</div>

<!-- partners -->
<div class="abs partners"></div>
<div class="abs arrow-sq" style="left:155px;top:1602px"><svg width="10" height="14" viewBox="0 0 10 14"><polyline points="7,2 2,7 7,12" fill="none" stroke="#fff" stroke-width="1.6"/></svg></div>
<div class="abs arrow-sq" style="left:1021px;top:1602px"><svg width="10" height="14" viewBox="0 0 10 14"><polyline points="3,2 8,7 3,12" fill="none" stroke="#fff" stroke-width="1.6"/></svg></div>
<div class="abs partner" style="left:213px;width:88px" role="img" aria-label="Partner badge"></div>
<div class="abs partner" style="left:375px;width:84px" role="img" aria-label="Partner badge"></div>
<div class="abs partner" style="left:520px;width:82px" role="img" aria-label="Partner badge"></div>
<div class="abs partner" style="left:664px;width:142px" role="img" aria-label="Partner badge"></div>
<div class="abs partner" style="left:858px;width:96px" role="img" aria-label="Partner badge"></div>

<!-- get in touch -->
<section class="abs touch">
  <h2>GET IN TOUCH</h2>
  <div class="rule"></div>
  <div class="knot"></div>
  <p>Lorem Ipsum is simply dummy text of the printing and typestting industry. Lorem Ipsum has been the industry's</p>
</section>
<div class="abs map" role="img" aria-label="Street map of the surrounding towns"></div>
<div class="abs pin"><svg width="22" height="28" viewBox="0 0 22 28"><path d="M11 1C5.5 1 1.5 5 1.5 10.3 1.5 17 11 27 11 27s9.5-10 9.5-16.7C20.5 5 16.5 1 11 1z" fill="#fff"/><circle cx="11" cy="10.3" r="3.6" fill="#e2401c"/></svg></div>
<div class="abs info">
  <div class="mark"><i></i><span>WOHNKARTA</span></div>
  <ul>
    <li><svg width="8" height="11" viewBox="0 0 8 11"><path d="M4 0.5C2 0.5 0.5 2 0.5 4 0.5 6.6 4 10.5 4 10.5S7.5 6.6 7.5 4C7.5 2 6 0.5 4 0.5z" fill="#555"/></svg><span>Adress goes here or city, state and<br>zipcode</span></li>
    <li><svg width="9" height="10" viewBox="0 0 9 10"><path d="M2 0.8 3.6 3 2.6 4.2C3.3 5.6 4.3 6.7 5.7 7.4L6.9 6.4 8.8 8 7.8 9.4C4 9 0.9 5.8 0.6 2z" fill="#555"/></svg><span>999-0000-000</span></li>
    <li class="mail"><svg width="10" height="8" viewBox="0 0 10 8"><rect x="0.5" y="0.5" width="9" height="7" fill="#555"/><polyline points="0.5,0.5 5,4.5 9.5,0.5" fill="none" stroke="#fff" stroke-width="1"/></svg><span>info@sahranigroup.com</span></li>
  </ul>
</div>

<!-- footer -->
<footer class="abs footer">
  <nav><span>Home</span><span>About</span><span>Browse</span><span>Salute</span><span>Blog</span><span>Community</span><span>Contact</span></nav>
  <div class="lang"><svg width="9" height="9" viewBox="0 0 9 9"><circle cx="4.5" cy="4.5" r="4" fill="#2a8cc8"/></svg>English ▾</div>
</footer>
<div class="abs base"></div>

</body>
</html>
```